Computer Service Provider in Need of New Letterhead Design

We are Quarrybell Computer Services, a computer/IT services company that provides IT Support, software, hardware, virus monitoring, etc. in Vermont. We are looking for new letterhead, that is both professional and matches the current theme of our business cards & website.
Please note that we want to include the following information:
www.Quarrybell.example
555-555-0147
47 Fernhollow Road, Cedarbrook, NX 00147
Thoughtful Support • Dependable Service • Lasting Reliability
I will be attaching our logo along with the business card images.
We would love to have the

```html
<!DOCTYPE html>
<html lang="en">
<head>
<meta charset="utf-8">
<title>Quarrybell Computer Services — Letterhead</title>
<link rel="stylesheet" href="https://fonts.googleapis.com/css2?family=Tinos:wght@400;700&family=Lato:wght@400;700&display=swap">
<style>
  :root {
    --backdrop: #6a6a6a;
    --paper: #fbfbfb;
    --brand-blue: #2b5a84;
    --accent-orange: #f0891e;
    --ink: #1a1a1a;
    --muted-ink: #555555;
    --band-text: #ffffff;
  }
  * { margin: 0; padding: 0; box-sizing: border-box; }
  html, body {
    width: 1200px; height: 1200px; overflow: hidden;
    background: var(--backdrop);
  }
  .letterhead {
    position: absolute; left: 232px; top: 48px;
    width: 736px; height: 1104px;
    background: var(--paper);
    font-family: "Tinos", "Times New Roman", serif;
    color: var(--ink);
  }
  .brand {
    position: absolute; left: 190px; top: 79px;
    display: flex; align-items: center; gap: 15px;
  }
  .brand-mark {
    width: 109px; height: 74px; background: var(--brand-blue);
  }
  .brand-name {
    font-family: "Lato", Arial, sans-serif; font-weight: 700;
    color: var(--brand-blue);
  }
  .brand-name .name-main { display: block; font-size: 34px; line-height: 36px; }
  .brand-name .name-sub { display: block; font-size: 16px; line-height: 18px; letter-spacing: 2.4px; }
  .letter-body {
    position: absolute; left: 67px; width: 604px;
    font-size: 14.8px; line-height: 17.7px;
  }
  .letter-body sup { font-size: 9px; line-height: 0; vertical-align: 5px; }
  .issue-date { top: 256px; }
  .recipient { top: 328px; }
  .reference { top: 436px; font-weight: 700; }
  .salutation { top: 507px; }
  .message { top: 543px; text-align: justify; }
  .message p + p { margin-top: 18px; }
  .closing { top: 758px; }
  .taglines {
    position: absolute; left: 64px; top: 968px;
    list-style: none;
    font-family: "Lato", Arial, sans-serif; font-size: 14.5px; line-height: 18px;
    color: var(--ink);
  }
  .taglines li::before {
    content: ""; display: inline-block; width: 5px; height: 5px; border-radius: 50%;
    background: var(--accent-orange); margin: 0 6px 3px 0;
  }
  .contacts {
    position: absolute; right: 30px; top: 986px;
    font-family: "Lato", Arial, sans-serif; font-size: 13px; line-height: 19px;
    color: var(--muted-ink); text-align: right;
  }
  .contacts div { display: flex; align-items: center; justify-content: flex-end; gap: 4px; }
  .contact-icon { width: 18px; height: 18px; }
  .address-band {
    position: absolute; left: 0; bottom: 0; width: 100%; height: 53px;
    background: var(--brand-blue); color: var(--band-text);
    font-family: "Lato", Arial, sans-serif; font-size: 15px;
    display: flex; align-items: center; justify-content: center;
  }
</style>
</head>
<body>
<main class="letterhead">
  <header class="brand">
    <div class="brand-mark"></div>
    <div class="brand-name">
      <span class="name-main">Quarrybell</span>
      <span class="name-sub">COMPUTER SERVICES</span>
    </div>
  </header>

  <p class="letter-body issue-date">Issuing date: May 5, 2012</p>
  <p class="letter-body recipient">Name of employee: Mr. xyz<br>Address of employee<br>address line 2</p>
  <p class="letter-body reference">Ref: Promotion as an Assistant secretary</p>
  <p class="letter-body salutation">Dear Mr. xyz,</p>
  <div class="letter-body message">
    <p>I have the pleasure to inform you that you have been promoted as assistant secretary in the share department of the company. You are required to take charge of the new assignment on 15<sup>th</sup> May, 2012. Please accept my hearty congratulations on your promotion.</p>
    <p>Your salary scale in the promoted cadre will be Tk. 16,000 and from 15th may, your basic salary will be fixed at Tk. 12,000 in the said scale. You will be entitled to all other allowances as applicable to the staff-II of the company. Other services conditions remain unchanged.</p>
    <p>Please acknowledge receipt of this letter.</p>
  </div>
  <p class="letter-body closing">Yours sincerely,</p>

  <ul class="taglines">
    <li>Thoughtful Support</li>
    <li>Dependable Service</li>
    <li>Lasting Reliability</li>
  </ul>

  <div class="contacts">
    <div>555-555-0147
      <svg class="contact-icon" viewBox="0 0 18 18" aria-hidden="true">
        <circle cx="9" cy="9" r="9" fill="#2b5a84"/>
        <path d="M5 7.5c0-1.5 8-1.5 8 0v1h-2v-1h-4v1H5z M6 9h6l1 4H5z" fill="#fff"/>
      </svg>
    </div>
    <div>www.Quarrybell.example
      <svg class="contact-icon" viewBox="0 0 18 18" aria-hidden="true">
        <circle cx="9" cy="9" r="9" fill="#2b5a84"/>
        <circle cx="9" cy="9" r="4.5" fill="none" stroke="#fff" stroke-width="1.3"/>
        <path d="M4.5 9h9M9 4.5c-2 2.5-2 6.5 0 9M9 4.5c2 2.5 2 6.5 0 9" fill="none" stroke="#fff" stroke-width="1"/>
      </svg>
    </div>
  </div>

  <footer class="address-band">47 Fernhollow Road, Cedarbrook, NX 00147</footer>
</main>
</body>
</html>
```